Business Card for a Floral & Decorating Business

I would like to take my current logo and create a better business card. I am looking for elegance as I am a florist and event decorator. My logo has multiple colour options. I like colours like green, purple, pink and orange, I think I would like a white card, open to black back ground. I want it to feel elegant and romantic. I like metallic lettering that maybe is indented in the paper, I also like glossy paper. I have a full logo already as well as a badge. I have attached both in multiple colours.m
Updates

Need extra days to review

Target Market(s)

Weddings, special events, floral customers

Industry/Entity Type

Floral and decorating

Contact Information for Business Card

Phone number, email, instagram, facebook, title, name, logo

Font styles to use
Script

Requirements
Nice to have
• Elegant

```html
<!DOCTYPE html>
<html lang="en">
<head>
<meta charset="utf-8">
<title>Halden Reeve – Business Card</title>
<link href="https://fonts.googleapis.com/css2?family=Montserrat:wght@400;500;700&family=Allura&display=swap" rel="stylesheet">
<style>
  :root {
    --stage: #e4e4e6;
    --card-dark: #1e1f1f;
    --card-green: #3f6e64;
    --card-green-light: #4b7c72;
    --teal: #3e7a6e;
    --teal-soft: #4c8275;
    --silver: #d6e0dd;
    --white: #f4f6f5;
    --divider: #5a5f5e;
  }
  * { box-sizing: border-box; margin: 0; padding: 0; }
  html, body { width: 1200px; height: 800px; overflow: hidden; }
  body {
    background: var(--stage);
    font-family: "Montserrat", sans-serif;
    display: flex;
    align-items: center;
    justify-content: center;
    gap: 40px;
  }
  .card {
    width: 540px;
    height: 310px;
    border-radius: 26px;
    position: relative;
    overflow: hidden;
    box-shadow: 0 10px 24px rgba(0,0,0,0.18);
  }
  /* Back: contact side */
  .card--contact { background: var(--card-dark); display: flex; }
  .contact-brand {
    width: 56%;
    display: flex;
    align-items: center;
    justify-content: center;
    gap: 12px;
  }
  .divider {
    width: 1px;
    margin: 40px 0;
    background: linear-gradient(to bottom, transparent, var(--divider), transparent);
  }
  .contact-details {
    flex: 1;
    padding: 58px 0 0 30px;
    color: var(--white);
  }
  .person-name {
    font-weight: 700;
    font-size: 21px;
    color: var(--teal);
    letter-spacing: 0.3px;
  }
  .person-title {
    font-family: "Allura", cursive;
    font-size: 30px;
    line-height: 1;
    margin: 0 0 12px 4px;
    color: var(--white);
  }
  .address { font-size: 12.5px; line-height: 1.4; margin-bottom: 8px; }
  .contact-list { list-style: none; font-size: 12.5px; line-height: 1.65; }
  .contact-list li { display: flex; align-items: center; gap: 8px; }
  .contact-list svg { width: 11px; height: 11px; flex: none; }

  .brand-mark {
    width: 16px; height: 16px;
    border-radius: 50%;
    flex: none;
  }
  .brand-name {
    font-family: "Montserrat", sans-serif;
    font-weight: 500;
    letter-spacing: 2px;
    white-space: nowrap;
  }
  .contact-brand .brand-mark { background: var(--teal); }
  .contact-brand .brand-name { color: var(--teal); font-size: 22px; }

  /* Front: logo side */
  .card--logo {
    background: linear-gradient(160deg, var(--card-green-light), var(--card-green) 60%);
    display: flex;
    flex-direction: column;
    align-items: center;
    justify-content: center;
    gap: 34px;
  }
  .logo-lockup { display: flex; align-items: center; gap: 14px; }
  .card--logo .brand-mark { background: var(--silver); width: 20px; height: 20px; }
  .card--logo .brand-name { color: var(--silver); font-size: 32px; }
  .social {
    display: flex; align-items: center; gap: 8px;
    color: var(--silver); font-size: 12.5px; letter-spacing: 0.6px;
  }
  .social-dot { width: 14px; height: 14px; border-radius: 50%; background: var(--silver); opacity: 0.8; }
</style>
</head>
<body>

  <section class="card card--contact" aria-label="Card back with contact details">
    <div class="contact-brand">
      <span class="brand-mark"></span>
      <span class="brand-name">Halden Reeve</span>
    </div>
    <div class="divider"></div>
    <div class="contact-details">
      <p class="person-name">Elliot Marsh</p>
      <p class="person-title">Florist</p>
      <p class="address">4120 Willow Bend Road<br>Juneau, Alaska 99801</p>
      <ul class="contact-list">
        <li>
          <svg viewBox="0 0 12 12" aria-hidden="true"><path fill="var(--teal-soft)" d="M2.5 0.8l2 2.2-1.1 1.3c.7 1.5 1.8 2.6 3.3 3.3L8 6.5l2.2 2-1.2 2.3C4.5 10.5 1.5 7.5 0.8 2z"/></svg>
          555-218-4790
        </li>
        <li>
          <svg viewBox="0 0 12 12" aria-hidden="true"><rect x="0.5" y="2" width="11" height="8" rx="1" fill="var(--teal-soft)"/><path d="M1 2.6l5 3.6 5-3.6" stroke="var(--card-dark)" stroke-width="1" fill="none"/></svg>
          hello@haldenreeve.com
        </li>
        <li>
          <svg viewBox="0 0 12 12" aria-hidden="true"><circle cx="6" cy="6" r="5.2" fill="var(--teal-soft)"/><path d="M1 6h10M6 0.8c-2 2.8-2 7.6 0 10.4M6 0.8c2 2.8 2 7.6 0 10.4" stroke="var(--card-dark)" stroke-width="0.8" fill="none"/></svg>
          www.haldenreeve.com
        </li>
      </ul>
    </div>
  </section>

  <section class="card card--logo" aria-label="Card front with business name">
    <div class="logo-lockup">
      <span class="brand-mark"></span>
      <span class="brand-name">Halden Reeve</span>
    </div>
    <div class="social">
      <span class="social-dot"></span>
      <span>@haldenreeve</span>
    </div>
  </section>

</body>
</html>
```